Template for Tolvik Advisory PowerPoint

We would like to create a new template for PowerPoint based on our current logo and graphic design guidelines. The template should reflect our corporate identity and be easy to use to create different kind of PowerPoint presentations for different kind of customers. The current design guideline that are attached reflect the "old" look of the PPT design and is only to be seen as a reference.
Tolvik Advisory is a Management consulting company working within both public and private sector. We focus on strategic business development and work in close cooperation with the customer to make sure it is the customer that will become the hero, our work is to support and guide them to the top.
The design should reflect a modern company working in close cooperation with our customers to help them innovate and describe their future business model, and also help them to reach that goal!
Words and taglines that we use. Passion for the future. The power of the organisation. Power of thoughts. Inspiration. Engagement.
What we have in mind is a modern, clean and elegant design based on our current logo. Tolvik Advisory is a Swedish Company working primarily on the Swedish market so the template must be possible to translate to Swedish (however the design can be done in english and be translated later)

Reason: I would like to extend the deadline to receive some more alternatives!

Reason: I'm out travelling and would like to extend the timeline to be able to choose the right design for our template. /Henrik

Target Market(s)

Our target market is within both private and public sector. Our main focus is CxO level executives within our clients organisation.

Industry/Entity Type

Management Consulting

Font styles to use
Sans Serif

Colors

Designer to choose colors to be used in the design.

Requirements
Must have
• A PPT template that contains both slides for traditional text and graphic. We like to work a lot with graphical presentations and try to limit the text on our slides to a minimum.
Nice to have
• Slides for different chapters within the presentation. Slides for powerful one-liners. Title slides. Thank you slides at the end.
Should not have
• Massive text....

```html
<!DOCTYPE html>
<html lang="en">
<head>
<meta charset="utf-8">
<title>Tolvik Advisory – Presentation Template</title>
<link rel="stylesheet" href="https://fonts.googleapis.com/css2?family=Questrial&display=swap">
<style>
  :root {
    --canvas: #ffffff;
    --board: #bfbfbf;
    --brand-red: #c8103a;
    --charcoal: #555555;
    --silver-light: #e8e8e8;
    --silver-dark: #a6a6a6;
    --white: #ffffff;
    --dot-grey: #d4d4d4;
    --shadow: rgba(0, 0, 0, 0.55);
  }
  html, body {
    margin: 0;
    padding: 0;
    width: 1200px;
    height: 1200px;
    overflow: hidden;
    background: var(--canvas);
    font-family: "Questrial", "Helvetica Neue", Arial, sans-serif;
  }
  .canvas {
    position: relative;
    width: 1200px;
    height: 1200px;
  }
  .board {
    position: absolute;
    left: 66px;
    top: 66px;
    width: 1065px;
    height: 1060px;
    background: var(--board);
  }
  .slide {
    position: absolute;
    width: 512px;
    height: 384px;
    box-shadow: 14px 18px 34px var(--shadow);
    overflow: hidden;
  }
  .slide svg {
    position: absolute;
    inset: 0;
    width: 512px;
    height: 384px;
  }
  .wordmark {
    position: absolute;
    margin: 0;
    font-weight: 400;
    white-space: nowrap;
    display: flex;
    align-items: center;
    gap: 6px;
    line-height: 1;
  }
  .wordmark .mark-dot {
    display: inline-block;
    border-radius: 50%;
    background: currentColor;
  }

  /* Content slide with red side band */
  .slide--sideband {
    left: 96px;
    top: 105px;
    background: linear-gradient(90deg, var(--silver-light) 0%, var(--silver-dark) 100%);
  }
  .slide--sideband .side-band {
    position: absolute;
    left: 0;
    top: 0;
    width: 161px;
    height: 100%;
    background: var(--brand-red);
  }
  .slide--sideband .wordmark {
    right: 6px;
    top: 20px;
    font-size: 19px;
    color: var(--brand-red);
  }
  .slide--sideband .mark-dot { width: 12px; height: 12px; }

  /* Title slide */
  .slide--title {
    left: 243px;
    top: 683px;
    background: var(--brand-red);
  }
  .slide--title .wordmark {
    left: 0;
    right: 0;
    top: 168px;
    justify-content: center;
    font-size: 44px;
    color: var(--white);
  }
  .slide--title .mark-dot { width: 26px; height: 26px; margin-left: 4px; }

  /* Text slide with header and footer bands */
  .slide--text {
    left: 553px;
    top: 345px;
    background: var(--white);
  }
  .slide--text .header-band {
    position: absolute;
    left: 0;
    top: 0;
    width: 100%;
    height: 48px;
    background: var(--charcoal);
  }
  .slide--text .footer-band {
    position: absolute;
    left: 0;
    bottom: 0;
    width: 100%;
    height: 46px;
    background: var(--brand-red);
  }
  .slide--text .wordmark {
    right: 6px;
    bottom: 12px;
    font-size: 19px;
    color: var(--white);
  }
  .slide--text .mark-dot { width: 12px; height: 12px; }

  .dotted {
    fill: none;
    stroke-width: 3.4;
    stroke-linecap: round;
    stroke-dasharray: 0 6;
  }
  .dotted--white { stroke: var(--white); }
  .dotted--grey { stroke: var(--dot-grey); }
</style>
</head>
<body>
<div class="canvas">
  <div class="board"></div>

  <section class="slide slide--sideband" aria-label="Content slide with red side band">
    <div class="side-band"></div>
    <svg viewBox="0 0 512 384" aria-hidden="true">
      <line class="dotted dotted--grey" x1="133" y1="29" x2="350" y2="29"/>
      <line class="dotted dotted--white" x1="5" y1="363" x2="315" y2="363"/>
    </svg>
    <p class="wordmark">Tolvik Advisory<span class="mark-dot"></span></p>
  </section>

  <section class="slide slide--title" aria-label="Title slide">
    <svg viewBox="0 0 512 384" aria-hidden="true">
      <line class="dotted dotted--white" x1="17" y1="146" x2="368" y2="146"/>
      <line class="dotted dotted--white" x1="145" y1="299" x2="496" y2="299"/>
    </svg>
    <p class="wordmark">Tolvik Advisory<span class="mark-dot"></span></p>
  </section>

  <section class="slide slide--text" aria-label="Text slide with header and footer bands">
    <div class="header-band"></div>
    <div class="footer-band"></div>
    <svg viewBox="0 0 512 384" aria-hidden="true">
      <line class="dotted dotted--grey" x1="275" y1="29" x2="504" y2="29"/>
      <line class="dotted dotted--white" x1="5" y1="366" x2="355" y2="366"/>
    </svg>
    <p class="wordmark">Tolvik Advisory<span class="mark-dot"></span></p>
  </section>
</div>
</body>
</html>
```